BEACON CABS

Taxi card design

Need changes very slow in replying to my messages.

Target Market(s)

Customers

Industry/Entity Type

Taxi

Contact Information for Business Card

See previous design

Font styles to use
Sans Serif

Colors
A7469A
B969AE
D3A5CF
EDDBEB
F8F0F9
6B429C
8869AF
B7A5CE
E3DAEB
F3F0F8

Requirements
Nice to have
• We are in the business of looking after people, not just driving vehicles front
Should not have
• Front number 01632 480 480 needs to big big

```html
<!DOCTYPE html>
<html lang="en">
<head>
<meta charset="utf-8">
<title>Beacon Cabs – Business Card</title>
<link rel="stylesheet" href="https://fonts.googleapis.com/css2?family=Exo+2:wght@600;700;800&family=Montserrat:wght@500;600;700&display=swap">
<style>
  :root{
    --purple-deep:#6B429C;
    --purple-mid:#8869AF;
    --magenta:#A7469A;
    --magenta-soft:#B969AE;
    --lilac:#D3A5CF;
    --mist:#F3F0F8;
    --ink:#2b2527;
    --ink-soft:#3d3537;
    --page:#ffffff;
  }
  *{margin:0;padding:0;box-sizing:border-box}
  html,body{width:687px;height:1200px;overflow:hidden;background:var(--page)}
  body{position:relative;font-family:"Montserrat",sans-serif;color:var(--ink)}
  .sprites{position:absolute;width:0;height:0;overflow:hidden}

  .card-slot{position:absolute;left:43px;width:601px;height:344px;box-shadow:0 3px 8px rgba(0,0,0,.18)}
  .card-slot--front{top:227px}
  .card-slot--back{top:630px}
  .card{position:absolute;left:0;top:0;width:944px;height:540px;transform:scale(.6366);transform-origin:0 0;overflow:hidden}
  .card__frame{position:absolute;inset:0;width:944px;height:540px}

  .brand-name{position:absolute;font-family:"Exo 2",sans-serif;font-weight:800;color:var(--ink);white-space:nowrap;letter-spacing:-.5px;display:flex;align-items:center;gap:18px;line-height:1}
  .brand-name__mark{display:inline-block;background:var(--magenta);border-radius:50%}

  .main-phone{position:absolute;display:flex;align-items:center;gap:20px;font-family:"Exo 2",sans-serif;font-weight:700;font-size:70px;color:var(--ink-soft);letter-spacing:1px;line-height:1;white-space:nowrap}
  .phone-badge{width:44px;height:44px;border-radius:9px;background:linear-gradient(135deg,var(--magenta),var(--purple-deep));display:flex;align-items:center;justify-content:center}
  .phone-badge svg{width:30px;height:30px;fill:#fff}

  /* front */
  .front .brand-name{left:0;right:0;top:208px;justify-content:center;font-size:80px}
  .front .brand-name__mark{width:40px;height:40px}
  .front .main-phone{left:208px;top:333px}

  /* back */
  .back .brand-name{left:54px;top:70px;font-size:56px}
  .back .brand-name__mark{width:28px;height:28px}
  .tagline-rule{position:absolute;left:58px;top:156px;width:182px;height:2px;background:var(--magenta)}
  .tagline-rule::before{content:"";position:absolute;left:-4px;top:-4px;width:10px;height:10px;border-radius:50%;background:var(--magenta)}
  .tagline{position:absolute;left:250px;top:150px;font-size:22px;font-weight:600;color:var(--ink-soft);white-space:nowrap}

  .services{position:absolute;left:0;top:0}
  .service{position:absolute;left:604px;font-size:22px;font-weight:700;letter-spacing:.6px;color:var(--ink-soft);white-space:nowrap;line-height:1}
  .service--air{top:55px}
  .service--mini{top:110px}
  .service--school{top:163px}

  .back .main-phone{left:208px;top:246px}

  .line-numbers{position:absolute;top:335px;left:0;width:944px;height:30px}
  .line-number{position:absolute;top:0;display:flex;align-items:center;gap:6px;font-family:"Exo 2",sans-serif;font-weight:700;font-size:25px;color:var(--ink-soft);white-space:nowrap;line-height:1}
  .line-number .phone-badge{width:18px;height:18px;border-radius:4px}
  .line-number .phone-badge svg{width:13px;height:13px}
  .line-number--one{left:61px}
  .line-number--two{left:358px}
  .line-number--three{left:661px}
  .line-sep{position:absolute;top:2px;width:1.5px;height:22px;background:#b9b3b5}
  .line-sep--a{left:322px}
  .line-sep--b{left:618px}
  .contact-rule{position:absolute;left:68px;top:369px;width:814px;height:2px;background:var(--magenta)}
  .contact-rule::before,.contact-rule::after{content:"";position:absolute;top:-4px;width:10px;height:10px;border-radius:50%;background:var(--magenta)}
  .contact-rule::before{left:-5px}
  .contact-rule::after{right:-5px}

  .contact-list{position:absolute;left:71px;top:394px;list-style:none;font-size:21px;font-weight:500;line-height:27.5px;color:var(--ink-soft);white-space:nowrap}
  .contact-list b{font-weight:700;color:var(--ink)}
  .address-pin{position:absolute;left:556px;top:398px;width:34px;height:44px}
  .address{position:absolute;left:604px;top:394px;font-style:normal;font-size:21px;font-weight:500;line-height:27.5px;color:var(--ink-soft);white-space:nowrap}
</style>
</head>
<body>

<svg class="sprites" aria-hidden="true">
  <defs>
    <symbol id="icon-phone" viewBox="0 0 24 24">
      <path d="M6.6 10.8c1.4 2.8 3.8 5.1 6.6 6.6l2.2-2.2c.3-.3.7-.4 1-.2 1.1.4 2.3.6 3.6.6.6 0 1 .4 1 1V20c0 .6-.4 1-1 1C10.6 21 3 13.4 3 4c0-.6.4-1 1-1h3.5c.6 0 1 .4 1 1 0 1.3.2 2.5.6 3.6.1.3 0 .7-.2 1z"/>
    </symbol>
    <linearGradient id="band-v" x1="0" y1="0" x2="0" y2="1">
      <stop offset="0" stop-color="#6B429C"/>
      <stop offset="1" stop-color="#A7469A"/>
    </linearGradient>
    <linearGradient id="band-h" x1="0" y1="0" x2="1" y2="0">
      <stop offset="0" stop-color="#A7469A"/>
      <stop offset=".75" stop-color="#6B429C"/>
      <stop offset="1" stop-color="#B969AE"/>
    </linearGradient>
    <linearGradient id="street-tone" x1="0" y1="0" x2="0" y2="1">
      <stop offset="0" stop-color="#ededed"/>
      <stop offset=".5" stop-color="#e4e4e4"/>
      <stop offset=".8" stop-color="#ece8dc"/>
      <stop offset="1" stop-color="#efefef"/>
    </linearGradient>
  </defs>
</svg>

<!-- Front of card -->
<div class="card-slot card-slot--front">
  <section class="card front">
    <svg class="card__frame" viewBox="0 0 944 540" aria-hidden="false">
      <rect width="944" height="540" fill="url(#band-v)"/>
      <polygon role="img" aria-label="Faded photo of a busy city street with yellow taxis"
        points="43,8 936,8 936,222 901,268 901,532 8,532 8,310 43,270" fill="url(#street-tone)"/>
    </svg>
    <h1 class="brand-name"><span class="brand-name__mark"></span>Beacon Cabs</h1>
    <p class="main-phone">
      <span class="phone-badge"><svg viewBox="0 0 24 24"><use href="#icon-phone"/></svg></span>
      01632 480 480
    </p>
  </section>
</div>

<!-- Back of card -->
<div class="card-slot card-slot--back">
  <section class="card back">
    <svg class="card__frame" viewBox="0 0 944 540">
      <rect width="944" height="540" fill="url(#band-v)"/>
      <rect role="img" aria-label="Faded photo of a busy city street with yellow taxis"
        x="8" y="8" width="928" height="502" fill="url(#street-tone)"/>
      <rect x="0" y="510" width="944" height="30" fill="url(#band-h)"/>
      <polygon points="742,510 762,510 792,540 772,540" fill="#ffffff"/>

      <!-- service timeline -->
      <line x1="564" y1="8" x2="564" y2="190" stroke="#A7469A" stroke-width="2"/>
      <g fill="#ffffff" stroke="#A7469A" stroke-width="2.5">
        <circle cx="564" cy="65" r="17"/>
        <circle cx="564" cy="120" r="17"/>
        <circle cx="564" cy="173" r="17"/>
      </g>
      <g fill="#A7469A">
        <!-- plane -->
        <path d="M553 66l9-2 6-7c1-1 3-1 3 1l-3 7 6 1 2-2h2l-1 4 1 4h-2l-2-2-6 1 3 7c0 2-2 2-3 1l-6-7-9-2z"/>
        <!-- minibus -->
        <rect x="553" y="113" width="22" height="11" rx="2"/>
        <circle cx="558" cy="126" r="2.5"/><circle cx="570" cy="126" r="2.5"/>
        <!-- school bus -->
        <rect x="555" y="163" width="18" height="18" rx="3"/>
        <rect x="558" y="166" width="12" height="6" fill="#ffffff"/>
      </g>
    </svg>

    <h2 class="brand-name"><span class="brand-name__mark"></span>Beacon Cabs</h2>
    <span class="tagline-rule"></span>
    <p class="tagline">24/7 Service</p>

    <ul class="services">
      <li class="service service--air">AIRPORT TRANSFERS</li>
      <li class="service service--mini">MINIBUSES</li>
      <li class="service service--school">SCHOOL TRANSPORT</li>
    </ul>

    <p class="main-phone">
      <span class="phone-badge"><svg viewBox="0 0 24 24"><use href="#icon-phone"/></svg></span>
      01632 480 480
    </p>

    <div class="line-numbers">
      <span class="line-number line-number--one"><span class="phone-badge"><svg viewBox="0 0 24 24"><use href="#icon-phone"/></svg></span>01632 96 06 60</span>
      <span class="line-sep line-sep--a"></span>
      <span class="line-number line-number--two"><span class="phone-badge"><svg viewBox="0 0 24 24"><use href="#icon-phone"/></svg></span>01632 96 02 20</span>
      <span class="line-sep line-sep--b"></span>
      <span class="line-number line-number--three"><span class="phone-badge"><svg viewBox="0 0 24 24"><use href="#icon-phone"/></svg></span>01632 96 08 11</span>
    </div>
    <span class="contact-rule"></span>

    <ul class="contact-list">
      <li><b>Free Phone:</b> 0800 555 0147</li>
      <li><b>Email:</b> bookings@beaconcabs.co.uk</li>
      <li><b>Website:</b> www.beaconcabs.co.uk</li>
    </ul>

    <svg class="address-pin" viewBox="0 0 34 44" aria-hidden="true">
      <path d="M17 2C9 2 3 8 3 16c0 10 14 26 14 26s14-16 14-26C31 8 25 2 17 2z" fill="#8869AF"/>
      <circle cx="17" cy="16" r="6" fill="#ffffff"/>
    </svg>
    <address class="address">Market Hall<br>12 Mill Lane Northbridge<br>NB4 7QD</address>
  </section>
</div>

</body>
</html>
```